I need a logo design for a new company based in Tucson called "Mindpilot Reg Holloway". I am a psychotherapist that specializes in clinical psychology with athletes and performers. The final design should incorporate the psychology symbol as a watermark. The logo should convey movement and fluidity. "Mindpilot" is a bit of a play on words combining psychology (head) with sports (coach). Other design interests include mid-century, Ansel Brigham Kotter. I will want to use the logo for business cards, letterhead and marketing brochures. I will put together a website at a later date. I am attaching a file with some pertinent information for the business card. Thank you.
Reg Holloway
mindpilotregholloway@quillmarsh.net
Updates

Thank you all for the submissions so far.  I have submitted an additional file with a draft of a new design idea.  Since "mindpilot" is a bit of a play on words, I would like to see something with the two "H's" look something like quotation marks.  If the psychology logo is to be included at all, it needs to be less prominent.     Thank you all.  Reg                               

Target Market(s)

1) Adolescent and adult athletes and performers who are looking to increase their level of performance (Sport and Performance Psychology)
2) Adult psychotherapy patients (Clinical psychology)

Industry/Entity Type

Marketing

Colors

Designer to choose colors to be used in the design.

Requirements
Must have
• 1) Since "mindpilot" is a bit of a play on words, The "H's" need to be in a font that looks somewhat like quotation marks.

Nice to have
• Logo on one side. All other info on the backside?

```html
<!DOCTYPE html>
<html lang="en">
<head>
<meta charset="utf-8">
<title>Mindpilot Reg Holloway – Business Card</title>
<link rel="stylesheet" href="https://fonts.googleapis.com/css2?family=Cinzel:wght@500&family=Oswald:wght@600&family=Open+Sans:wght@400;600&display=swap">
<style>
  :root {
    --backdrop: #ece9e3;
    --card-white: #ffffff;
    --card-shade: #eef0f1;
    --ink: #2b2b2b;
    --ink-soft: #555555;
    --rule-light: #c9cccf;
    --gold: #dfa923;
    --gold-deep: #c9951a;
    --gold-light: #e9bb3a;
  }
  html, body {
    margin: 0;
    padding: 0;
    width: 1200px;
    height: 1018px;
    overflow: hidden;
    background: var(--backdrop);
  }
  .canvas {
    position: relative;
    width: 1200px;
    height: 1018px;
  }
  .card {
    position: absolute;
    left: 250px;
    width: 700px;
    height: 400px;
    box-shadow: 0 6px 22px rgba(0,0,0,0.18);
  }
  .card-front {
    top: 70px;
    background: linear-gradient(135deg, var(--card-white) 0%, var(--card-white) 45%, var(--card-shade) 100%);
  }
  .card-back {
    top: 540px;
    background: linear-gradient(135deg, var(--gold-light) 0%, var(--gold) 50%, var(--gold-deep) 100%);
  }
  .brand-mark {
    position: absolute;
    left: 46px;
    top: 72px;
    width: 100px;
    height: 100px;
    border-radius: 50%;
    background: radial-gradient(circle at 40% 35%, var(--gold-light), var(--gold-deep));
  }
  .brand-name {
    position: absolute;
    left: 168px;
    top: 104px;
    margin: 0;
    font-family: "Cinzel", serif;
    font-weight: 500;
    font-size: 25px;
    letter-spacing: 1.5px;
    line-height: 1;
    color: var(--ink);
    white-space: nowrap;
  }
  .title-rule {
    position: absolute;
    left: 178px;
    top: 206px;
    width: 300px;
    height: 3px;
    background: var(--ink);
  }
  .band-rule {
    position: absolute;
    left: 0;
    top: 206px;
    width: 178px;
    height: 1px;
    background: var(--rule-light);
  }
  .side-rule {
    position: absolute;
    left: 590px;
    top: 0;
    width: 1px;
    height: 400px;
    background: var(--rule-light);
  }
  .person {
    position: absolute;
    left: 60px;
    top: 228px;
  }
  .person-name {
    margin: 0;
    font-family: "Oswald", sans-serif;
    font-weight: 600;
    font-size: 30px;
    letter-spacing: 1px;
    color: var(--ink);
    line-height: 1.1;
  }
  .person-role {
    margin: 2px 0 0;
    font-family: "Open Sans", sans-serif;
    font-size: 12px;
    letter-spacing: 1.5px;
    color: var(--ink-soft);
  }
  .contact {
    position: absolute;
    left: 60px;
    top: 312px;
    margin: 0;
    padding: 0;
    list-style: none;
    display: grid;
    grid-template-columns: 170px 260px;
    row-gap: 9px;
    font-family: "Open Sans", sans-serif;
    font-size: 12.5px;
    color: var(--ink);
  }
  .contact li {
    display: flex;
    align-items: center;
    gap: 7px;
    white-space: nowrap;
  }
  .contact .wide {
    grid-column: 1 / span 2;
  }
  .contact svg {
    width: 12px;
    height: 12px;
    flex: none;
  }
</style>
</head>
<body>
<main class="canvas">
  <section class="card card-front" aria-label="Business card front">
    <div class="brand-mark" aria-hidden="true"></div>
    <h1 class="brand-name">Mindpilot Reg Holloway</h1>
    <div class="band-rule"></div>
    <div class="title-rule"></div>
    <div class="side-rule"></div>
    <div class="person">
      <p class="person-name">IVO MARLOW</p>
      <p class="person-role">GENERAL MANAGER</p>
    </div>
    <ul class="contact">
      <li>
        <svg viewBox="0 0 12 12" aria-hidden="true"><path d="M2.5 1h2l1 3-1.4 1a6 6 0 0 0 2.9 2.9L8 6.5l3 1v2A1.5 1.5 0 0 1 9.5 11 8.5 8.5 0 0 1 1 2.5 1.5 1.5 0 0 1 2.5 1z" fill="#2b2b2b"/></svg>
        014 552 7390
      </li>
      <li>
        <svg viewBox="0 0 12 12" aria-hidden="true"><rect x="1" y="2.5" width="10" height="7" fill="#2b2b2b"/><path d="M1 2.5l5 4 5-4" stroke="#fff" stroke-width="1" fill="none"/></svg>
        ivo@quillmarsh.net
      </li>
      <li>
        <svg viewBox="0 0 12 12" aria-hidden="true"><rect x="2.5" y="1" width="7" height="10" rx="1" fill="none" stroke="#2b2b2b" stroke-width="1.3"/></svg>
        014 552 7390
      </li>
      <li>
        <svg viewBox="0 0 12 12" aria-hidden="true"><circle cx="6" cy="6" r="5" fill="none" stroke="#2b2b2b" stroke-width="1.1"/><path d="M1 6h10M6 1c-2.5 3-2.5 7 0 10M6 1c2.5 3 2.5 7 0 10" fill="none" stroke="#2b2b2b" stroke-width="0.9"/></svg>
        www.mindpilotnotes.net
      </li>
      <li class="wide">42 Larkspur Road, 2nd floor Suite B.</li>
    </ul>
  </section>
  <section class="card card-back" aria-label="Business card back"></section>
</main>
</body>
</html>
```